Walking Beside the Quiet River; A Study of Refuge, Purpose & Calling

I need a book cover, for the above book title. This is a journey of the heart to know the heart of God. I think on the text, Simple (see below graphic)
Black Lettering for Knowing.....Intimately
Gold lettering for God
Either gold or black for the subtitle; A Study of Refuge, Purpose, & Calling
I would like the below graphic idea only no photograph of a person,
and White background instead of black
Simple Font, like below graphic, but open to suggestions

Target Market(s)

not age specific, Every person has been given a heart to know God, we are taking the mystery out the process to understand God is Father, loving gracious, ever present, etc. If we know His heart, we realize He's not at a distance, He is there, an ever present help

Industry/Entity Type

Security

Requirements
Must have
• Title: Walking Beside the Quiet River; A Study of Refuge, Purpose, & Calling
• My name, Tom Pettigrew
Nice to have
• See Below Graphic

```html
<!DOCTYPE html>
<html lang="en">
<head>
<meta charset="utf-8">
<title>Walking Beside the Quiet River — Book Cover</title>
<link rel="stylesheet" href="https://fonts.googleapis.com/css2?family=Montserrat:wght@400;500&display=swap">
<style>
  :root {
    --page-bg: #ffffff;
    --ink: #141008;
    --ink-soft: #1e1709;
    --title-accent: rgba(74, 50, 8, 0.78);
    --glow-core: #fff6c8;
    --glow-inner: #ffe07a;
    --glow-mid: #f2b533;
    --glow-outer: #d98a12;
    --glow-edge: #8a4a08;
  }
  * { box-sizing: border-box; margin: 0; padding: 0; }
  html, body {
    width: 1200px;
    height: 1200px;
    overflow: hidden;
    background: var(--page-bg);
  }
  .canvas {
    position: relative;
    width: 1200px;
    height: 1200px;
  }
  .book-cover {
    position: absolute;
    left: 255px;
    top: 60px;
    width: 690px;
    height: 1080px;
    overflow: hidden;
    font-family: 'Montserrat', Arial, sans-serif;
    color: var(--ink);
    text-align: center;
  }
  .cover-art {
    position: absolute;
    inset: 0;
    background:
      radial-gradient(ellipse 42% 32% at 50% 50%, var(--glow-core) 0%, rgba(255, 230, 140, 0.75) 45%, rgba(255, 220, 110, 0) 100%),
      radial-gradient(ellipse 95% 75% at 50% 50%, var(--glow-inner) 0%, var(--glow-mid) 40%, var(--glow-outer) 72%, var(--glow-edge) 115%);
  }
  .cover-title {
    position: absolute;
    left: 0;
    right: 0;
    top: 300px;
    font-weight: 500;
    font-size: 74px;
    line-height: 1.22;
    letter-spacing: 1px;
    text-transform: uppercase;
  }
  .cover-title .line { display: block; }
  .cover-title .accent { color: var(--title-accent); }
  .cover-subtitle {
    position: absolute;
    left: 0;
    right: 0;
    top: 630px;
    font-weight: 400;
    font-size: 35px;
    line-height: 1.3;
    color: var(--ink-soft);
  }
  .cover-author {
    position: absolute;
    left: 0;
    right: 0;
    top: 905px;
    font-weight: 500;
    font-size: 32px;
    letter-spacing: 5px;
    text-transform: uppercase;
  }
</style>
</head>
<body>
  <main class="canvas">
    <section class="book-cover">
      <div class="cover-art" role="img" aria-label="Radiant golden light bursting outward from a small figure at the centre"></div>
      <h1 class="cover-title">
        <span class="line">Walking</span>
        <span class="line accent">Beside the</span>
        <span class="line">Quiet River</span>
      </h1>
      <p class="cover-subtitle">A Study of Refuge,<br>Purpose &amp; Calling</p>
      <p class="cover-author">Tom Pettigrew</p>
    </section>
  </main>
</body>
</html>
```